Modern Proposal / Estimate Template for Vehicle Wrap Company (Coat Comet)

Project Overview

We are looking for creative designers to develop a modern proposal / estimate template for our vehicle wrap company, Coat Comet.

This will be used repeatedly as our standard proposal format when presenting vehicle wrap projects to potential clients.

We are NOT looking for a basic invoice or QuickBooks-style estimate.

This should feel like a professional marketing piece that helps sell the project and impress the client.

What We Want

We want designers to propose new creative layout concepts using our logo and brand as the foundation, but we encourage original design ideas and graphics.

I am including some of logos and images for reference. You can also visit www.thecoatcomet.com to get a feel for our branding. We want you to use this as a baseline...but we are looking for fresh, new takes on our existing brand. Be creative please!

The final design should feel:

• Modern
• Bold
• Professional
• Clean
• Sales-focused

Think agency presentation rather than basic estimate document.

Template Purpose

The template should allow our team to easily customize proposals for each project.

The layout should include space for things like:

• Client logo
• Client company name
• Vehicle wrap mockups or design ideas
• Fleet details (vehicles, locations, logistics)
• Pricing breakdown

This template will be reused over and over, so the design should be structured but flexible.

Typical Proposal Sections

Design should allow space for sections like:

• Cover page
• Project overview
• Why work with Coat Comet
• Scope of work
• Vehicle / fleet breakdown
• Pricing / investment
• Next steps

You do not need to fill all content, but the layout should support these elements.

Creative Direction

We want designers to think about how to visually communicate:

• Vehicle branding
• Fleet marketing
• mobile advertising
• professional installation

Graphics, icons, and layout structure are where we are hoping to see creative input.

Important

Please do NOT simply recreate a basic estimate sheet.

We want creative concepts for a proposal layout that feels like a marketing presentation.

Designs that stand out visually while remaining clean and professional will be most successful.

Final Deliverable

A reusable proposal template layout that Coat Comet can customize for different clients and projects.

Editable design files preferred.

```html
<!DOCTYPE html>
<html lang="en">
<head>
<meta charset="utf-8">
<title>Coat Comet – Vehicle Wrap Proposal</title>
<link href="https://fonts.googleapis.com/css2?family=Arimo:wght@400;700&family=Barlow:wght@500;700;800&display=swap" rel="stylesheet">
<style>
:root{
  --slate:#2e3a3f;
  --orange:#d0532a;
  --grey:#cfcfcf;
  --mid-grey:#5e6368;
  --light:#e6e7e8;
  --ink:#111;
  --white:#fff;
}
*{box-sizing:border-box;margin:0;padding:0}
html,body{width:1200px;height:5348px;overflow:hidden;background:var(--white)}
body{position:relative;font-family:"Arimo",Arial,sans-serif;color:var(--ink)}
.slide{position:absolute;left:0;width:1200px;height:712px;overflow:hidden;background:var(--white);border:1px solid #bbb}
.slide svg.bg{position:absolute;inset:0;width:100%;height:100%}
.page-no{position:absolute;right:14px;bottom:10px;color:var(--white);font:700 30px "Arimo",Arial,sans-serif}
.rule{width:94px;height:7px;background:var(--orange);margin-top:14px}
.brand-name{font-family:"Barlow",Arial,sans-serif;font-weight:800;letter-spacing:2px}
.body-copy{font-size:18.5px;line-height:25px;font-weight:700}

/* cover */
.cover{top:0;background:var(--slate);border:none}
.cover .brand-name{position:absolute;left:74px;top:92px;font-size:52px;color:var(--slate)}
.cover .title{position:absolute;left:74px;top:334px;color:var(--white);font:800 88px/78px "Barlow",Arial,sans-serif;letter-spacing:1px}
.cover .for{position:absolute;left:76px;top:594px;color:var(--white);font:500 30px "Barlow",Arial,sans-serif}

/* about */
.about{top:768px}
.about .heading{position:absolute;left:740px;top:62px;font:700 42px/38px "Arimo",Arial,sans-serif}
.about .heading .sub{display:block;color:var(--orange);font-size:30px;line-height:38px}
.about .copy{position:absolute;left:740px;top:240px;width:440px}
.about .copy p{margin-bottom:20px}

/* overview */
.overview{top:1538px}
.overview h2{position:absolute;left:48px;top:62px;color:var(--white);font:700 60px/58px "Arimo",Arial,sans-serif}
.overview .rule{position:absolute;left:48px;top:188px;margin:0}
.overview ul{position:absolute;left:560px;top:104px;width:600px;list-style:none}
.overview li{position:relative;padding-left:24px;margin-bottom:32px}
.overview li::before{content:"";position:absolute;left:0;top:7px;width:12px;height:12px;border-radius:50%;background:var(--orange)}

/* mockups */
.mockups{top:2312px}
.slide-title{position:absolute;left:48px;top:36px}
.slide-title h2{font:700 52px/60px "Arimo",Arial,sans-serif}
.mockups .intro{position:absolute;left:52px;top:146px;width:450px;font:700 14px/19px "Arimo",Arial,sans-serif}
.mockups .intro ul{list-style:none;margin-top:8px;padding-left:16px}
.mockups .intro li::before{content:"";display:inline-block;width:6px;height:6px;border-radius:50%;background:var(--orange);margin-right:4px;vertical-align:middle}
.mockup{position:absolute;top:270px;width:538px;height:350px}
.mockup.van{left:60px}
.mockup.truck{left:623px}

/* tables */
.pricing{top:3088px}
.fleet{top:3862px}
table.sheet{position:absolute;left:52px;width:1084px;border-collapse:collapse;font-size:20px;table-layout:fixed}
table.sheet th,table.sheet td{border:1.5px solid var(--slate);height:48px}
table.sheet th{color:var(--white);font-weight:700;line-height:20px;text-align:center;background:var(--orange);height:79px}
table.sheet th.desc{background:var(--slate);text-align:left;padding-left:18px}
table.sheet td.label{background:var(--light);font-weight:700;padding-left:18px}
table.sheet td.dark{background:var(--slate);border-left:2px solid var(--white)}
.pricing table.sheet{top:192px}
.fleet table.sheet{top:158px}
.col-desc{width:544px}
.col-num{width:180px}

/* next steps */
.next{top:4636px;border:none}
.next .brand-name{position:absolute;left:70px;top:330px;width:340px;text-align:center;font-size:54px;color:var(--white)}
.next h2{position:absolute;left:650px;top:236px;font:700 52px "Arimo",Arial,sans-serif}
.next .copy{position:absolute;left:652px;top:322px;width:440px}
.next .contact{position:absolute;left:650px;top:404px;font:700 20px/34px "Arimo",Arial,sans-serif}
.next .contact div{display:flex;align-items:center;gap:6px}
.next .contact svg{width:24px;height:24px}
</style>
</head>
<body>

<svg width="0" height="0" style="position:absolute">
  <defs>
    <radialGradient id="studioGrad" cx="50%" cy="45%" r="65%">
      <stop offset="0" stop-color="#6a6a6a"/>
      <stop offset=".35" stop-color="#3a3a3a"/>
      <stop offset=".75" stop-color="#151515"/>
      <stop offset="1" stop-color="#050505"/>
    </radialGradient>
    <linearGradient id="coverGrad" x1="0" y1="0" x2="1" y2="1">
      <stop offset="0" stop-color="#1b1b1b"/>
      <stop offset=".45" stop-color="#4d4f52"/>
      <stop offset=".7" stop-color="#2a2b2d"/>
      <stop offset="1" stop-color="#0a0a0a"/>
    </linearGradient>
    <linearGradient id="yardGrad" x1="0" y1="0" x2="0" y2="1">
      <stop offset="0" stop-color="#8e97a3"/>
      <stop offset=".28" stop-color="#b7bcc3"/>
      <stop offset=".4" stop-color="#9a5a44"/>
      <stop offset=".52" stop-color="#2b2d30"/>
      <stop offset=".72" stop-color="#3d3f42"/>
      <stop offset=".85" stop-color="#77797c"/>
      <stop offset="1" stop-color="#5c5e61"/>
    </linearGradient>
    <linearGradient id="shopGrad" x1="0" y1="0" x2="0" y2="1">
      <stop offset="0" stop-color="#d8d8d8"/>
      <stop offset=".25" stop-color="#8f8f8f"/>
      <stop offset=".55" stop-color="#3a3c3e"/>
      <stop offset=".8" stop-color="#5a2a24"/>
      <stop offset="1" stop-color="#bdbdbd"/>
    </linearGradient>
  </defs>
</svg>

<!-- Cover -->
<section class="slide cover">
  <svg class="bg" viewBox="0 0 1200 712">
    <rect x="0" y="0" width="560" height="272" fill="#fff"/>
    <polygon role="img" aria-label="Photo of a wrapped black cargo van on a dark studio background" points="560,0 1200,0 1200,712 790,712 510,240" fill="url(#coverGrad)"/>
    <polygon points="480,0 560,0 430,272 350,272" fill="#cfcfcf"/>
    <polygon points="460,200 560,200 520,272 420,272" fill="#d0532a"/>
    <polygon points="500,270 545,210 820,712 770,712" fill="#d0532a"/>
  </svg>
  <div class="brand-name">COAT COMET</div>
  <h1 class="title">VEHICLE<br>WRAP<br>PROPOSAL</h1>
  <p class="for">FOR: [Client Name] / [Date]</p>
</section>

<!-- About -->
<section class="slide about">
  <svg class="bg" viewBox="0 0 1200 712">
    <rect role="img" aria-label="Photo of a fleet of wrapped vans parked in front of the company building" x="0" y="0" width="706" height="712" fill="url(#yardGrad)"/>
    <polygon points="1200,596 1200,712 1132,712" fill="#d0532a"/>
  </svg>
  <h2 class="heading">About<br>COAT COMET<span class="sub">Vehicle Wrap</span></h2>
  <div class="copy body-copy">
    <p>Lorem ipsum dolor sit amet, consectetur adipiscing elit. Sed do eiusmod tempor incididunt ut labore et dolore magna aliqua.</p>
    <p>Lorem ipsum dolor sit amet, consectetur adipiscing elit. Sed do eiusmod tempor incididunt ut labore et dolore magna aliqua.</p>
    <p>Lorem ipsum dolor sit amet, consectetur adipiscing elit. Sed do eiusmod tempor incididunt ut labore et dolore magna aliqua.</p>
  </div>
  <span class="page-no">1</span>
</section>

<!-- Project overview -->
<section class="slide overview">
  <svg class="bg" viewBox="0 0 1200 712">
    <polygon points="0,0 505,0 345,251 0,251" fill="#2e3a3f"/>
    <polygon role="img" aria-label="Photo of a wrapped van parked in front of a workshop" points="0,251 345,251 444,444 345,610 0,610" fill="url(#shopGrad)"/>
    <polygon points="345,610 444,444 588,712 0,712 0,610" fill="#2e3a3f"/>
    <polygon points="0,520 90,712 0,712" fill="#d0532a"/>
    <polygon points="110,610 250,610 190,712 60,712" fill="#d0532a"/>
    <polygon points="1200,596 1200,712 1132,712" fill="#d0532a"/>
  </svg>
  <h2>Project<br>Overview</h2>
  <div class="rule"></div>
  <ul class="body-copy">
    <li>Lorem ipsum dolor sit amet, consectetur adipiscing elit. Sed do eiusmod tempor incididunt ut labore et dolore magna aliqua.</li>
    <li>Lorem ipsum dolor sit amet, consectetur adipiscing elit. Sed do eiusmod tempor incididunt ut labore et dolore magna aliqua.</li>
    <li>Lorem ipsum dolor sit amet, consectetur adipiscing elit. Sed do eiusmod tempor incididunt ut labore et dolore magna aliqua.</li>
    <li>Lorem ipsum dolor sit amet, consectetur adipiscing elit. Sed do eiusmod tempor incididunt ut labore et dolore magna aliqua.</li>
    <li>Lorem ipsum dolor sit amet, consectetur adipiscing elit. Sed do eiusmod tempor incididunt ut labore et dolore magna aliqua.</li>
  </ul>
  <span class="page-no">2</span>
</section>

<!-- Vehicle mockups -->
<section class="slide mockups">
  <svg class="bg" viewBox="0 0 1200 712">
    <polygon points="1050,0 1200,0 1200,150" fill="#d0532a"/>
    <polygon points="1130,60 1200,180 1200,260 1090,100" fill="#2e3a3f"/>
    <polygon points="1200,596 1200,712 1132,712" fill="#d0532a"/>
  </svg>
  <div class="slide-title"><h2>Vehicle Mockups</h2><div class="rule"></div></div>
  <div class="intro">
    Lorem ipsum dolor sit amet, consectetur adipiscing elit. Sed do eiusmod tempor incididunt ut labore et dolore magna aliqua.
    <ul><li>Vehicle Design</li><li>Mockup Design</li></ul>
  </div>
  <svg class="mockup van" viewBox="0 0 538 350" role="img" aria-label="Mockup of a wrapped van, side view"><rect width="538" height="350" fill="url(#studioGrad)"/></svg>
  <svg class="mockup truck" viewBox="0 0 538 350" role="img" aria-label="Mockup of a wrapped pickup truck, side view"><rect width="538" height="350" fill="url(#studioGrad)"/></svg>
  <span class="page-no">3</span>
</section>

<!-- Pricing -->
<section class="slide pricing">
  <svg class="bg" viewBox="0 0 1200 712"><polygon points="1200,596 1200,712 1132,712" fill="#d0532a"/></svg>
  <div class="slide-title"><h2>Pricing &amp; Investment</h2><div class="rule"></div></div>
  <table class="sheet">
    <colgroup><col class="col-desc"><col class="col-num"><col class="col-num"><col class="col-num"></colgroup>
    <tr><th class="desc">Description</th><th>Prior<br>Investment</th><th>Periodically<br>Investment</th><th>Total<br>Investment</th></tr>
    <tr><td></td><td></td><td></td><td></td></tr>
    <tr><td></td><td></td><td></td><td></td></tr>
    <tr><td></td><td></td><td></td><td></td></tr>
    <tr><td></td><td></td><td></td><td></td></tr>
    <tr><td></td><td></td><td></td><td></td></tr>
    <tr><td class="label">TOTAL:</td><td class="dark"></td><td class="dark"></td><td class="dark"></td></tr>
  </table>
  <span class="page-no">4</span>
</section>

<!-- Fleet -->
<section class="slide fleet">
  <svg class="bg" viewBox="0 0 1200 712">
    <polygon points="1050,0 1200,0 1200,150" fill="#d0532a"/>
    <polygon points="1130,60 1200,180 1200,260 1090,100" fill="#2e3a3f"/>
    <polygon points="1200,596 1200,712 1132,712" fill="#d0532a"/>
  </svg>
  <div class="slide-title"><h2>Fleet Breakdown</h2><div class="rule"></div></div>
  <table class="sheet">
    <colgroup><col class="col-desc"><col class="col-num"><col class="col-num"><col class="col-num"></colgroup>
    <tr><th class="desc">Description</th><th>Vehicle</th><th>Fleet</th><th>Total</th></tr>
    <tr><td></td><td></td><td></td><td></td></tr>
    <tr><td></td><td></td><td></td><td></td></tr>
    <tr><td></td><td></td><td></td><td></td></tr>
    <tr><td></td><td></td><td></td><td></td></tr>
    <tr><td></td><td></td><td></td><td></td></tr>
    <tr><td></td><td></td><td></td><td></td></tr>
    <tr><td></td><td></td><td></td><td></td></tr>
    <tr><td></td><td></td><td></td><td></td></tr>
    <tr><td class="label">TOTAL:</td><td></td><td></td><td></td></tr>
  </table>
  <span class="page-no">5</span>
</section>

<!-- Next steps -->
<section class="slide next">
  <svg class="bg" viewBox="0 0 1200 712">
    <rect width="1200" height="712" fill="#fff"/>
    <polygon points="0,0 660,0 420,712 0,712" fill="#2e3a3f"/>
    <polygon points="300,0 540,0 420,300" fill="#5e6368"/>
    <polygon points="0,580 150,712 0,712" fill="#d0532a"/>
    <polygon points="200,560 500,560 420,712 300,712" fill="#d0532a"/>
    <polygon points="500,560 580,360 740,712 420,712" fill="#2e3a3f"/>
    <polygon points="1200,596 1200,712 1132,712" fill="#d0532a"/>
  </svg>
  <div class="brand-name">COAT COMET</div>
  <h2>Next Steps</h2>
  <p class="copy body-copy">Lorem ipsum dolor sit amet, consectetur adipiscing elit. Sed do eiusmod tempor incididunt ut labore et dolore magna aliqua.</p>
  <div class="contact">
    <div><svg viewBox="0 0 24 24" aria-hidden="true"><circle cx="12" cy="12" r="11" fill="#d0532a"/><circle cx="12" cy="12" r="7" fill="none" stroke="#fff" stroke-width="1.6"/><path d="M5 12h14M12 5c-3 4-3 10 0 14M12 5c3 4 3 10 0 14" stroke="#fff" stroke-width="1.4" fill="none"/></svg>www.coatcomet.com</div>
    <div><svg viewBox="0 0 24 24" aria-hidden="true"><circle cx="12" cy="12" r="11" fill="#d0532a"/><path d="M8 6l2.5 3-1.5 1.5c.8 1.8 2.3 3.3 4.2 4.2L14.7 13l3 2.5-1.6 2.2C11 17 7 13 6.2 7.8z" fill="#fff"/></svg>xxx - xxx - xxx</div>
  </div>
  <span class="page-no">6</span>
</section>

</body>
</html>
```